Law firm business card

Information:

Me Miriam Dufresne

website: dufresne-law.ca
email: miriam@dufresne-law.ca
Phone: 514 555-0147
Fax: 514 555-0183

Address:
Dufresne and associates
2719 Belcourt
Montreal, QC
H2K 3M9

Areas of Expertise:
Franchise Agreements, Financing, Acquisition, Real Estate Development, Commercial Agreements and Corporate Law

Target Market(s)

executives, companie managers

Industry/Entity Type

Business

Colors
f78f20
000000

Requirements
Must have
• Must use the logo, the logo is available here:

https://www.filebinder-example.com/sh/qxt8rr2ka41wpe/BBKtm7Lwzve_pQRYdNG_HJcWb

```html
<!DOCTYPE html>
<html lang="en">
<head>
<meta charset="utf-8">
<title>Dufresne &amp; Associates – Business Card</title>
<link rel="stylesheet" href="https://fonts.googleapis.com/css2?family=Cinzel:wght@600;700&display=swap">
<style>
  :root {
    --card-orange: #ff6a00;
    --ink-white: #ffffff;
  }
  html, body {
    margin: 0;
    padding: 0;
    width: 1200px;
    height: 741px;
    overflow: hidden;
    background: var(--card-orange);
  }
  .card {
    position: relative;
    width: 1200px;
    height: 741px;
    background: var(--card-orange);
    color: var(--ink-white);
    font-family: "Cinzel", serif;
    font-weight: 700;
  }
  .card > * { position: absolute; margin: 0; line-height: 1; }
  .firm-mark { left: 85px; top: 89px; }
  .firm-divider { left: 270px; top: 86px; width: 3px; height: 146px; background: var(--ink-white); }
  .firm-name {
    left: 303px; top: 108px;
    font-size: 68px;
    letter-spacing: 1px;
  }
  .firm-tagline {
    left: 349px; top: 175px;
    font-size: 35px;
    letter-spacing: 5px;
  }
  .rule { left: 122px; width: 959px; height: 3px; background: var(--ink-white); }
  .rule-top { top: 320px; }
  .rule-bottom { top: 447px; }
  .lawyer-name {
    left: 200px; width: 860px; top: 342px;
    text-align: center;
    font-size: 74px;
    letter-spacing: 1px;
  }
  .contact-list, .office-address {
    font-size: 27px;
    line-height: 33px;
    list-style: none;
    padding: 0;
  }
  .contact-list { left: 68px; top: 465px; }
  .contact-divider { left: 577px; top: 463px; width: 2px; height: 156px; background: var(--ink-white); }
  .office-address { left: 602px; top: 464px; font-style: normal; }
</style>
</head>
<body>
<main class="card">
  <svg class="firm-mark" width="140" height="140" viewBox="0 0 140 140" aria-hidden="true">
    <circle cx="70" cy="70" r="66" fill="none" stroke="#ffffff" stroke-width="4"/>
  </svg>
  <div class="firm-divider"></div>
  <p class="firm-name">DUFRESNE</p>
  <p class="firm-tagline">&amp; ASSOCIATES</p>

  <div class="rule rule-top"></div>
  <h1 class="lawyer-name">Miriam Dufresne</h1>
  <div class="rule rule-bottom"></div>

  <ul class="contact-list">
    <li>website: dufresne-law.ca</li>
    <li>email: miriam@dufresne-law.ca</li>
    <li>Phone: 514 555-0147</li>
    <li>Fax: 514 555-0183</li>
  </ul>
  <div class="contact-divider"></div>
  <address class="office-address">
    Lakeshore Legal Resource<br>
    Centre Inc.<br>
    2719 Belcourt<br>
    Montreal, QC<br>
    H2K 3M9
  </address>
</main>
</body>
</html>
```